3D Printing Website redesign

We are in the process of redesigning our website. Attached is an image of one of the proposed pages - "The Quotewheel". The idea with this page is that site visitors can get an indicative estimate of the cost of 3D Printing based on some provided metrics. When the user alters the metrics the price changes accordingly. We are looking for a design to support this page that will also be used across our site.

Industry/Entity Type

Printing

```html
<!DOCTYPE html>
<html lang="en">
<head>
<meta charset="utf-8">
<title>Layerform Studio – The Quotewheel</title>
<link rel="stylesheet" href="https://fonts.googleapis.com/css2?family=Source+Sans+3:wght@400;600;700&family=Archivo+Black&display=swap">
<style>
:root{
  --page:#f4f4f5;
  --nav:#1f4a8a;
  --nav-line:#3a63a0;
  --cyan:#00b6f0;
  --mid-blue:#1d65a8;
  --panel:#283f6b;
  --ink:#0f1230;
  --track:#d9d9dc;
  --muted-label:#b9c2d4;
  --field:#e1e1ea;
  --field-text:#2a2f4a;
  --required:#e0483b;
  --heading:#2868b0;
  --mark:#9aa2b8;
}
*{box-sizing:border-box;margin:0;padding:0}
html,body{width:1200px;height:999px;overflow:hidden}
body{background:var(--page);font-family:"Source Sans 3",Arial,sans-serif;position:relative}
.abs{position:absolute}
.util-btn{top:0;width:50px;height:35px;background:var(--nav);display:flex;align-items:center;justify-content:center}
.main-nav{left:0;top:112px;width:1200px;height:57px;background:var(--nav);box-shadow:0 3px 4px rgba(0,0,0,.25)}
.nav-item{top:0;height:57px;display:flex;align-items:center;justify-content:center;color:#fff;font-weight:600;font-size:15px;border-left:1px solid var(--nav-line);white-space:nowrap}
.nav-item.active{background:var(--cyan);border-color:var(--cyan)}
.brand-mark{left:500px;top:10px;width:195px;height:195px;border-radius:50%;background:var(--mark)}
.brand-name{left:710px;top:36px;width:380px;color:var(--nav);font-weight:700;font-size:44px;line-height:1;white-space:nowrap}
.quote-banner{left:330px;top:212px;width:558px;height:49px;background:#e4e4ec;border:1px solid #d0d0dc;display:flex;align-items:center;justify-content:center}
.banner-text{font-family:"Archivo Black",Arial,sans-serif;color:var(--heading);font-size:32px;line-height:1;letter-spacing:3px;white-space:nowrap;text-shadow:1px 2px 2px rgba(0,0,0,.35)}
.banner-or{left:0;top:268px;width:1200px;text-align:center;line-height:1}
.quote-panel{left:0;top:310px;width:1200px;height:498px;background:var(--panel);box-shadow:0 4px 5px rgba(0,0,0,.45)}
.service-btn{left:102px;width:245px;height:109px;display:flex;align-items:center;justify-content:center;color:#fff;font-weight:700;font-size:50px}
.label{color:#fff;font-size:30px;font-weight:400;text-align:center;width:300px;left:487px;line-height:1}
.side-label{color:var(--muted-label);font-size:24px;line-height:1}
.track{left:450px;width:310px;height:25px;background:var(--track)}
.thumb{top:0;width:24px;height:25px;background:var(--cyan)}
.step{width:31px;height:25px;background:var(--ink);display:flex;align-items:center;justify-content:center;border-left:1px solid #2a2f50}
.select{left:450px;top:714px;width:372px;height:40px;background:var(--field)}
.select-arrow{right:0;top:0;width:40px;height:40px;background:var(--ink);display:flex;align-items:center;justify-content:center}
.preview{left:877px;top:408px;width:220px;height:220px;border-radius:50%;background:var(--ink)}
.total{left:857px;top:649px;width:260px;text-align:center;color:#fff;font-size:15px;font-weight:600}
.field{left:259px;width:300px;height:40px;background:var(--field);color:var(--field-text);font-size:16px;padding-left:15px;display:flex;align-items:center}
.field.focused{border:2px solid #c5c5cf;padding-left:13px}
.req{color:var(--required);margin-left:3px}
.captcha-image{left:639px;top:862px;width:300px;height:72px;background:var(--field)}
</style>
</head>
<body>
  <div class="abs util-btn" style="left:103px">
    <svg width="22" height="20" viewBox="0 0 22 20"><circle cx="11" cy="6" r="5" fill="#fff"/><path d="M1 20c0-6 4-8 10-8s10 2 10 8z" fill="#fff"/></svg>
  </div>
  <div class="abs util-btn" style="left:157px">
    <svg width="18" height="18" viewBox="0 0 18 18"><circle cx="7" cy="7" r="5.5" fill="none" stroke="#fff" stroke-width="2"/><line x1="11" y1="11" x2="16.5" y2="16.5" stroke="#fff" stroke-width="2.4"/></svg>
  </div>

  <nav class="abs main-nav">
    <div class="abs nav-item" style="left:103px;width:75px">HOME</div>
    <div class="abs nav-item" style="left:178px;width:80px">SHOP</div>
    <div class="abs nav-item active" style="left:258px;width:87px">PRICES</div>
    <div class="abs nav-item" style="left:345px;width:122px">MATERIALS</div>
    <div class="abs nav-item" style="left:715px;width:95px">GALLERY</div>
    <div class="abs nav-item" style="left:810px;width:105px">TRAINING</div>
    <div class="abs nav-item" style="left:915px;width:105px">ABOUT US</div>
    <div class="abs nav-item" style="left:1020px;width:77px;border-right:1px solid var(--nav-line)">BLOG</div>
  </nav>

  <div class="abs brand-mark"></div>
  <div class="abs brand-name">Layerform Studio</div>

  <div class="abs quote-banner"><span class="banner-text">GET AN INSTANT QUOTE</span></div>
  <div class="abs banner-or"><span class="banner-text">OR</span></div>

  <section class="abs quote-panel"></section>

  <div class="abs service-btn" style="top:382px;background:var(--cyan)">PRINT</div>
  <div class="abs service-btn" style="top:513px;background:var(--mid-blue)">SCAN</div>
  <div class="abs service-btn" style="top:645px;background:var(--ink)">DESIGN</div>

  <div class="abs label" style="top:343px">SHAPES</div>
  <div class="abs side-label" style="left:423px;top:357px">SQUARE</div>
  <div class="abs side-label" style="left:736px;top:357px">CIRCULAR</div>
  <div class="abs track" style="top:390px"><div class="abs thumb" style="left:156px"></div></div>
  <div class="abs step" style="left:760px;top:390px"><svg width="8" height="10"><path d="M6 1 2 5l4 4" fill="none" stroke="#fff" stroke-width="1.6"/></svg></div>
  <div class="abs step" style="left:791px;top:390px"><svg width="8" height="10"><path d="M2 1l4 4-4 4" fill="none" stroke="#fff" stroke-width="1.6"/></svg></div>

  <div class="abs label" style="top:450px">SIZE</div>
  <div class="abs track" style="top:496px"><div class="abs thumb" style="left:236px"></div></div>
  <div class="abs step" style="left:760px;top:496px"><svg width="8" height="10"><path d="M6 1 2 5l4 4" fill="none" stroke="#fff" stroke-width="1.6"/></svg></div>
  <div class="abs step" style="left:791px;top:496px"><svg width="8" height="10"><path d="M2 1l4 4-4 4" fill="none" stroke="#fff" stroke-width="1.6"/></svg></div>

  <div class="abs label" style="top:565px">VOLUME</div>
  <div class="abs track" style="top:611px"><div class="abs thumb" style="left:86px"></div></div>
  <div class="abs step" style="left:761px;top:611px"><svg width="8" height="10"><path d="M6 1 2 5l4 4" fill="none" stroke="#fff" stroke-width="1.6"/></svg></div>
  <div class="abs step" style="left:792px;top:611px"><svg width="8" height="10"><path d="M2 1l4 4-4 4" fill="none" stroke="#fff" stroke-width="1.6"/></svg></div>

  <div class="abs label" style="top:661px">MATERIAL</div>
  <div class="abs select">
    <div class="abs select-arrow"><svg width="14" height="10"><path d="M2 2l5 5 5-5" fill="none" stroke="#fff" stroke-width="2.2"/></svg></div>
  </div>

  <div class="abs preview"></div>
  <div class="abs total">Quotewheel Total: $35*</div>

  <div class="abs field focused" style="top:862px">Name<span class="req">*</span></div>
  <div class="abs field" style="top:920px">Email<span class="req">*</span></div>
  <div class="abs field" style="top:978px">Phone<span class="req">*</span></div>

  <div class="abs captcha-image" role="img" aria-label="Captcha verification image"></div>
  <div class="abs field" style="left:639px;top:954px">Enter captcha<span class="req">*</span></div>
</body>
</html>
```